We need an eye catching logo design and Business Card that portrays our business, which is the cleaning and protecting of stainless steel with an organic non chemical product. This can be separate to the company name or can incorporate it. Maybe even just the company name itself. Company Name is Gleamwise Gleamwise.
Ideal for products exposed to weather elements, ie: balustrading, enclosures, BBQs, we also supply the product so you can do it yourself (DIY).
In addition we would want to include on this card:
1. My Name (Paul Dremmick)
2. Mobile No. (TBA Later)
3. Email address (TBA Later)
4. Web address (TBA Later)
Updates

Please note that we also need suggestions on a logo, as this we do not have this either.

Please note we have update our brief to be more specific.

Thank You.

Paul

Reason: Awaiting for a couple of revised submissions from feedback given.

Target Market(s)

Purchasing officers and government people.

Industry/Entity Type

Steel

Colors

Designer to choose colors to be used in the design.

Requirements
Must have
• 1. Name (Paul Dremmick)
2. Mobile No. (TBA Later)
Should not have
• Should not be to busy looking

```html
<!DOCTYPE html>
<html lang="en">
<head>
<meta charset="utf-8">
<title>Gleamwise Gleamwise – Business Card</title>
<link rel="stylesheet" href="https://fonts.googleapis.com/css2?family=Lato:wght@400;700;900&display=swap">
<style>
  :root {
    --backdrop: #ececec;
    --card-steel: #9b9b9b;
    --card-steel-light: #a6a6a6;
    --card-steel-dark: #939393;
    --ink-soft: #d9d9d9;
    --ink-bright: #f4f4f4;
  }
  html, body {
    margin: 0;
    padding: 0;
    width: 1200px;
    height: 1000px;
    overflow: hidden;
    background: var(--backdrop);
  }
  .stage {
    position: relative;
    width: 1200px;
    height: 1000px;
    background: var(--backdrop);
  }
  .business-card {
    position: absolute;
    left: 168px;
    top: 258px;
    width: 862px;
    height: 486px;
    border-radius: 30px;
    background:
      repeating-linear-gradient(0deg, rgba(255,255,255,0.035) 0 1px, rgba(0,0,0,0.03) 1px 2px, transparent 2px 4px),
      linear-gradient(180deg, var(--card-steel-light), var(--card-steel) 50%, var(--card-steel-dark));
    font-family: "Lato", sans-serif;
    color: var(--ink-soft);
  }
  .holder-name {
    position: absolute;
    left: 32px;
    top: 52px;
    margin: 0;
    font-size: 26px;
    font-weight: 400;
    letter-spacing: 1px;
    color: var(--ink-soft);
  }
  .holder-name .first-name {
    font-weight: 900;
  }
  .brand-name {
    position: absolute;
    right: 24px;
    top: 138px;
    margin: 0;
    font-size: 92px;
    font-weight: 900;
    letter-spacing: -1px;
    line-height: 1;
    color: var(--ink-bright);
  }
  .contact-list {
    position: absolute;
    left: 30px;
    bottom: 18px;
    margin: 0;
    padding: 0;
    list-style: none;
    font-size: 20px;
    line-height: 33px;
  }
  .contact-list .label {
    display: inline-block;
    width: 40px;
    font-weight: 900;
  }
  .website {
    position: absolute;
    right: 22px;
    bottom: 18px;
    margin: 0;
    font-size: 20px;
    line-height: 33px;
  }
  .website strong {
    font-weight: 900;
  }
</style>
</head>
<body>
  <main class="stage">
    <section class="business-card" aria-label="Gleamwise Gleamwise business card">
      <h1 class="holder-name"><span class="first-name">PAUL</span> DREMMICK</h1>
      <p class="brand-name">GLEAMWISE</p>
      <ul class="contact-list">
        <li><span class="label">M</span>1-800-GLEAMWISE</li>
        <li><span class="label">E</span>paul@gleamwisegleamwise.com</li>
      </ul>
      <p class="website">www.<strong>gleamwisegleamwise</strong>.com</p>
    </section>
  </main>
</body>
</html>
```